Real Estate Company / Capital Needs Cards!

need business cards designed using the logos that were just designed by sketchhive.

Reason: per designers request deadline extended 1 day…thank you.

Target Market(s)

Investors and clients looking to purchase real estate or invest in the business.

Industry/Entity Type

Business

Requirements
Must have
• two designs - one for the real estate logo and one for the capital logo, similar but slightly different.
Nice to have
• something to make it pop (perhaps on the back)
Should not have
• much color

```html
<!DOCTYPE html>
<html lang="en">
<head>
<meta charset="utf-8">
<title>Corvan Business Cards</title>
<link rel="stylesheet" href="https://fonts.googleapis.com/css2?family=Lato:wght@400;700&display=swap">
<style>
  :root {
    --backdrop: #dcd7d0;
    --card-dark: #111112;
    --card-light: #ffffff;
    --ink: #1d1d1d;
    --ink-soft: #3a3a3a;
    --mark-grey: #7a7a7c;
    --mark-white: #ffffff;
  }
  * { margin: 0; padding: 0; box-sizing: border-box; }
  html, body { width: 1200px; height: 900px; overflow: hidden; }
  body {
    position: relative;
    background: var(--backdrop);
    font-family: "Lato", sans-serif;
    color: var(--ink);
  }
  .card {
    position: absolute;
    border-radius: 14px;
    box-shadow: 0 3px 8px rgba(0,0,0,0.25);
    text-align: center;
  }
  .card--dark { background: var(--card-dark); color: var(--mark-white); }
  .card--light { background: var(--card-light); }

  .capital-back  { left: 20px;  top: 77px;  width: 285px; height: 486px; }
  .capital-front { left: 317px; top: 77px;  width: 283px; height: 484px; }
  .estate-back   { left: 610px; top: 370px; width: 284px; height: 486px; }
  .estate-front  { left: 907px; top: 370px; width: 283px; height: 485px; }

  .abs { position: absolute; left: 0; right: 0; }

  .brand-square { position: absolute; border-radius: 4px; }
  .brand-name {
    position: absolute;
    font-weight: 400;
    letter-spacing: 0.12em;
    text-transform: uppercase;
    line-height: 1.05;
  }

  /* Capital back */
  .capital-back .brand-square { left: 100px; top: 248px; width: 85px; height: 85px; background: var(--mark-white); }
  .capital-back .brand-name { left: 0; right: 0; top: 345px; font-size: 27px; color: var(--mark-white); }
  .capital-back .brand-name small { display: block; font-size: 27px; }

  .website { font-size: 14px; letter-spacing: 0.01em; }
  .capital-back .website { top: 433px; }
  .website b { font-weight: 700; }

  /* Capital front */
  .capital-front .brand-square { left: 105px; top: 45px; width: 68px; height: 68px; background: var(--mark-grey); }
  .capital-front .brand-name { left: 0; right: 0; top: 122px; font-size: 20px; color: var(--mark-grey); }

  .person-name { font-size: 15px; color: var(--ink); }
  .person-role { font-size: 12px; color: var(--ink-soft); letter-spacing: 0.04em; }
  .contact { font-size: 11.5px; color: var(--ink-soft); line-height: 16.5px; }

  .capital-front .person-name { top: 224px; }
  .capital-front .person-role { top: 244px; }
  .capital-front .address { top: 336px; }
  .capital-front .phones  { top: 384px; }
  .capital-front .email   { top: 434px; }

  /* Estate back */
  .estate-back .brand-square { left: 23px; top: 313px; width: 72px; height: 72px; background: var(--mark-white); }
  .estate-back .brand-name { left: 108px; top: 322px; font-size: 25px; color: var(--mark-white); text-align: left; }
  .estate-back .website { top: 434px; }

  /* Estate front */
  .estate-front .brand-square { left: 48px; top: 71px; width: 58px; height: 58px; background: var(--mark-grey); }
  .estate-front .brand-name { left: 118px; top: 78px; font-size: 22px; color: var(--mark-grey); text-align: left; }
  .estate-front .person-name { top: 224px; }
  .estate-front .person-role { top: 244px; }
  .estate-front .address { top: 336px; }
  .estate-front .phones  { top: 384px; }
  .estate-front .email   { top: 434px; }
</style>
</head>
<body>

  <section class="card card--dark capital-back">
    <span class="brand-square"></span>
    <p class="brand-name">Corvan<small>Capital, LLC</small></p>
    <p class="abs website">www.<b>corvancapital</b>.com</p>
  </section>

  <section class="card card--light capital-front">
    <span class="brand-square"></span>
    <p class="brand-name">Corvan Capital, LLC</p>
    <p class="abs person-name">Paul Marsh</p>
    <p class="abs person-role">CEO</p>
    <p class="abs contact address">Harbour View Office ,<br>Portside, South Africa.</p>
    <p class="abs contact phones">Tel: +27 (11) 5550142<br>Mob: +27 700 555 019</p>
    <p class="abs contact email">Email: info@corvancapital.com</p>
  </section>

  <section class="card card--dark estate-back">
    <span class="brand-square"></span>
    <p class="brand-name">Corvan<br>Real Estate</p>
    <p class="abs website">www.<b>corvanrealestate</b>.com</p>
  </section>

  <section class="card card--light estate-front">
    <span class="brand-square"></span>
    <p class="brand-name">Corvan<br>Real Estate</p>
    <p class="abs person-name">Paul Marsh</p>
    <p class="abs person-role">CEO</p>
    <p class="abs contact address">Harbour View Office ,<br>Portside, South Africa.</p>
    <p class="abs contact phones">Tel: +27 (11) 5550142<br>Mob: +27 700 555 019</p>
    <p class="abs contact email">Email: info@corvanrealestate.com</p>
  </section>

</body>
</html>
```